Business Card Design

We have our logo and everything in place. Looking to have a layout for our new business cards designed. These will be printed with a matte finish, possibly rounded corners, and looking to incorporate some cool spot UV layers into the design.

Ive uploaded the existing card front and back as well as our logo.

Card Size Will Be 3.5" x 2"

```html
<!DOCTYPE html>
<html lang="en">
<head>
<meta charset="utf-8">
<title>Ridgeline Deck and Rail – Business Cards</title>
<link href="https://fonts.googleapis.com/css2?family=Open+Sans:ital,wght@0,400;1,400&display=swap" rel="stylesheet">
<style>
  :root {
    --stage: #03212f;
    --card-back: #1f1f20;
    --card-front: #0b0b0b;
    --ink-white: #ffffff;
    --ink-soft: #e6e6e6;
    --spot-uv: #2c2c2e;
  }
  * { margin: 0; padding: 0; box-sizing: border-box; }
  html, body {
    width: 1200px; height: 1099px; overflow: hidden;
    background: var(--stage);
    font-family: "Open Sans", Arial, sans-serif;
  }
  .sheet {
    position: relative; width: 1200px; height: 1099px;
  }
  .card {
    position: absolute; left: 180px; width: 840px; height: 480px;
    border-radius: 10px; overflow: hidden;
  }
  .card--back { top: 50px; background: var(--card-back); }
  .card--front { top: 569px; background: var(--card-front); color: var(--ink-white); }

  .spot-name {
    position: absolute; left: 0; right: 0; top: 178px;
    text-align: center; color: var(--spot-uv);
    font-size: 52px; line-height: 1.15; font-weight: 400;
  }
  .spot-name span { display: block; font-size: 20px; letter-spacing: 4px; }

  .holder { position: absolute; left: 46px; top: 40px; }
  .holder__name { font-size: 30px; font-weight: 400; line-height: 1.2; }
  .holder__title { font-size: 18px; font-style: italic; color: var(--ink-soft); }

  .brand-name {
    position: absolute; right: 60px; top: 180px; width: 320px;
    text-align: center; color: var(--ink-white);
    font-size: 46px; line-height: 1.15; font-weight: 400;
  }
  .brand-name span { display: block; font-size: 17px; letter-spacing: 4px; }

  .contact {
    position: absolute; right: 46px; bottom: 34px;
    list-style: none; text-align: right;
  }
  .contact__item {
    display: flex; justify-content: flex-end; align-items: center; gap: 14px;
    font-size: 22px; line-height: 34px;
  }
  .contact__icon { width: 20px; height: 20px; fill: var(--ink-white); }
</style>
</head>
<body>
<main class="sheet">
  <section class="card card--back" aria-label="Card back">
    <p class="spot-name">Ridgeline<span>DECK AND RAIL</span></p>
  </section>

  <section class="card card--front" aria-label="Card front">
    <div class="holder">
      <h1 class="holder__name">Daniel Reyes</h1>
      <p class="holder__title">President</p>
    </div>

    <p class="brand-name">Ridgeline<span>DECK AND RAIL</span></p>

    <ul class="contact">
      <li class="contact__item">403.555.0172
        <svg class="contact__icon" viewBox="0 0 20 20" aria-hidden="true"><path d="M3 6c0-2 2-3 7-3s7 1 7 3v2h-4V6H7v2H3zM5 9h10l2 8H3z"/></svg>
      </li>
      <li class="contact__item">www.ridgelinedeckandrail.com
        <svg class="contact__icon" viewBox="0 0 20 20" aria-hidden="true"><circle cx="10" cy="10" r="8" fill="none" stroke="#fff" stroke-width="2"/><path d="M2 10h16M10 2c3 3 3 13 0 16M10 2c-3 3-3 13 0 16" fill="none" stroke="#fff" stroke-width="1.5"/></svg>
      </li>
      <li class="contact__item">hello@ridgelinedeckandrail.com
        <svg class="contact__icon" viewBox="0 0 20 20" aria-hidden="true"><rect x="2" y="4" width="16" height="12" rx="1"/><path d="M2 5l8 6 8-6" fill="none" stroke="#000" stroke-width="1.5"/></svg>
      </li>
    </ul>
  </section>
</main>
</body>
</html>
```